Fern Vale Ridgecrest Music Festival Poster

We are a summer music festival with concerts spanning Jazz, Cabaret, Education, Broadway, Chamber and Opera. We are looking for our key art for the 2016 season. This design will serve as the basis for all promotional materials, the concert program, and our web materials. Though eventually this means we will need to adjust the design to fit many different sizes, our poster will be printed mostly on 8.5" x 11" paper, and we can adapt from there. The design will be featured online and in print. It should be vertical and not landscape.

WE ARE SEEKING SLEEK, ELEGANT DESIGNS WITH MAYBE A KEY STOCK PHOTOGRAPH AND THE RELEVANT TEXT/DETAILS.

PLEASE NOTE: The included file "avenir logo.psd" is just a suggestion for the feel we are going for. It is our "working logo" after having scraped our old logo. We are interested in seeing your own ideas on how to style the brand name, but if you have ideas working with this version of the logo, feel free to use it.

REQUIRED DETAILS:
Festival Name: Fern Vale Ridgecrest Music Festival
Dates: July 29 - August 7 2016 (the year, 2016, must be included on the poster, but it does not need to be in the same location as where the actual dates are listed)
Website: www.fernvaleridgecrestfest.org

Additional Information:
- the 7 musical styles (jazz, choral, cabaret, education, broadway, chamber, opera) are important to defining who we are. You may decide to include these on the poster.
- We are looking for a very elegant design

TARGET:
We depend highly on an older clientele. We are working to expand our brand into younger demographics, but we want to be sure that we do not alienate our current consumer base with text that may be difficult for them to read.

Project Deadline Extended Reason: I am extending the deadline because it is taking longer to get feedback from my superiors than I had expected. Extending the deadline will give me time to provide adequate feedback from the people who will ultimately be making the decision. Thank you. Added Saturday, January 30, 2016

Sorry for the delay. There were issues with the decision makers but we are selecting in the next 24 hours.

Target Market(s)

Lovers of the styles of music we feature. We have a good number of elderly consumers, but also families and school groups (discussed further in description section)

Industry/Entity Type

Entertainment

Font styles to use
Sans Serif

Requirements
Must have
• Festival Name: Fern Vale Ridgecrest Music Festival
• Dates: July 29 - August 7 2016 (the year, 2016, must be included on the poster, but it does not need to be in the same location as where the actual dates are listed)
• Website: www.fernvaleridgecrestfest.org
Nice to have
• - the 7 musical styles (jazz, choral, cabaret, education, broadway, chamber, opera) are important to defining who we are. We would love to include these styles somewhere on the image, or feature them somehow in the artwork
• - Our brand has an elegance to it due to the type of music we offer, and our location being in a very natural space. inclusion of the music/nature mixed aspect of our brand in artwork might be nice
Should not have
• Anything that may offend or alienate an older, more conservative demographic

```html
<!DOCTYPE html>
<html lang="en">
<head>
<meta charset="utf-8">
<title>Fern Vale Ridgecrest Music Festival 2016</title>
<link rel="stylesheet" href="https://fonts.googleapis.com/css2?family=Bebas+Neue&family=Oswald:wght@300;400;500&display=swap">
<style>
  :root {
    --page: #d9dcde;
    --ink: #1b2326;
    --teal-light: #a9dcd6;
    --teal: #3f9fae;
    --teal-deep: #17566b;
    --navy: #0e2a3c;
    --amber: #e08a2c;
    --ember: #c4561c;
    --sage: #5f8a6a;
    --band: #2e5548;
    --bar: #f3f5f4;
    --text-light: #eef3ee;
    --accent-line: #3ab3d9;
  }
  * { margin: 0; padding: 0; box-sizing: border-box; }
  html, body {
    width: 1200px; height: 932px; overflow: hidden;
    background: var(--page);
  }
  .poster {
    position: absolute; left: 320px; top: 36px;
    width: 560px; height: 860px; overflow: hidden;
    background: var(--teal-deep);
    box-shadow: 0 10px 30px rgba(0,0,0,.25);
  }
  .poster-art {
    position: absolute; inset: 0;
    background:
      radial-gradient(circle at 50% 30%, rgba(30,30,35,.55) 0 70px, transparent 140px),
      radial-gradient(ellipse at 70% 68%, rgba(224,138,44,.85), transparent 40%),
      radial-gradient(ellipse at 30% 60%, rgba(196,86,28,.55), transparent 35%),
      radial-gradient(ellipse at 85% 25%, rgba(200,210,110,.45), transparent 40%),
      linear-gradient(180deg, var(--teal-light) 0%, var(--teal) 28%, var(--teal-deep) 55%, var(--sage) 72%, var(--navy) 100%);
  }
  .title-block {
    position: absolute; top: 88px; left: 0; width: 100%;
    text-align: center;
  }
  .title-rule {
    width: 440px; height: 2px; margin: 0 auto;
    background: rgba(255,255,255,.7);
  }
  .festival-name {
    font-family: "Bebas Neue", sans-serif;
    font-size: 64px; line-height: 1; letter-spacing: 1px;
    color: var(--ink); padding: 8px 0 6px;
  }
  .festival-sub {
    font-family: "Oswald", sans-serif; font-weight: 400;
    font-size: 36px; line-height: 1; color: var(--ember);
    margin-top: 10px; letter-spacing: 1px;
  }
  .date-bar {
    position: absolute; top: 318px; left: 0; width: 100%; height: 34px;
    background: linear-gradient(90deg, rgba(243,245,244,.6), var(--bar) 20%, var(--bar) 80%, rgba(243,245,244,.6));
    font-family: "Oswald", sans-serif; font-weight: 500;
    font-size: 22px; line-height: 34px; letter-spacing: 3px;
    color: var(--ink); text-align: center;
  }
  .year {
    position: absolute; top: 372px; left: 0; width: 100%;
    text-align: center;
    font-family: "Oswald", sans-serif; font-weight: 400;
    font-size: 270px; line-height: 1; letter-spacing: -4px;
    color: rgba(14,42,60,.55);
    -webkit-text-stroke: 4px var(--ink);
  }
  .styles-band {
    position: absolute; top: 660px; left: 0; width: 100%; height: 90px;
    background: linear-gradient(180deg, rgba(46,85,72,.85), rgba(30,70,70,.9));
    border-top: 3px solid var(--accent-line);
    border-bottom: 3px solid var(--accent-line);
    font-family: "Oswald", sans-serif; font-weight: 300;
    font-size: 30px; line-height: 40px; letter-spacing: 1px;
    color: var(--text-light); text-align: center; padding-top: 4px;
  }
  .website {
    position: absolute; top: 766px; left: 0; width: 100%;
    text-align: center;
    font-family: "Oswald", sans-serif; font-weight: 400;
    font-size: 19px; letter-spacing: 2px; color: var(--text-light);
  }
</style>
</head>
<body>
  <main class="poster">
    <div class="poster-art" role="img" aria-label="Key art: silhouetted jazz musicians around a vinyl record, with glowing light rays, mountain landscape and orange flame swirls in teal and amber tones"></div>

    <header class="title-block">
      <div class="title-rule"></div>
      <h1 class="festival-name">Fern Vale Ridgecrest</h1>
      <div class="title-rule"></div>
      <p class="festival-sub">MUSIC FESTIVAL</p>
    </header>

    <p class="date-bar">JULY 29 - AUGUST 7</p>

    <p class="year">2016</p>

    <p class="styles-band">JAZZ | CHORAL | CABARET | EDUCATION<br>BROADWAY | CHAMBER | OPERA</p>

    <p class="website">WWW.FERNVALERIDGECRESTFEST.ORG</p>
  </main>
</body>
</html>
```